Quorenta - Automated robotic Inspection with AI need new business cards

We need a new design of our business cards. The company is focused on automated quality control at high speed with unmatched results. We have a logo but need a more forward leaning business card that shows that we are delivering cutting edge technology.

Contact Information for Business Card

Name
Position
Adress
Phone
Email
e.g.
Lotta Berglund
Chief Financial Officer (CFO)

Quorenta Sweden AB
Rönnvägen 14, SE-175 43 JÄRFÄLLA, Sweden
Mobile: +46701 23 45 67 | Office: +46 8 52 61 74
www.quorenta-example.com

Font styles to use
Sans Serif

```html
<!DOCTYPE html>
<html lang="en">
<head>
<meta charset="utf-8">
<title>Quorenta business card</title>
<link href="https://fonts.googleapis.com/css2?family=Bebas+Neue&family=Arimo:wght@400&display=swap" rel="stylesheet">
<style>
  :root {
    --bg: #2b2b2d;
    --card-white: #f4f4f3;
    --brand-blue: #1a4f7e;
    --brand-blue-deep: #133d63;
    --name-blue: #1b4a80;
    --ink: #1c1c1c;
  }
  * { margin: 0; padding: 0; box-sizing: border-box; }
  html, body { width: 1200px; height: 900px; overflow: hidden; }
  body {
    background: var(--bg);
    position: relative;
    font-family: "Arimo", Arial, sans-serif;
  }
  .card {
    position: absolute;
    left: 280px;
    width: 640px;
    height: 366px;
  }
  .card--front { top: 60px; background: var(--card-white); color: var(--ink); }
  .card--back { top: 474px; background: var(--brand-blue); }

  .identity { position: absolute; left: 62px; top: 112px; }
  .identity__name {
    font-family: "Bebas Neue", "Arial Narrow", sans-serif;
    font-size: 46px;
    line-height: 1;
    letter-spacing: 0.5px;
    color: var(--name-blue);
    font-weight: 400;
  }
  .identity__role { font-size: 17px; margin-top: 2px; }

  .divider {
    position: absolute;
    left: 330px; top: 150px;
    width: 1.5px; height: 96px;
    background: var(--name-blue);
  }

  .contacts {
    position: absolute;
    left: 350px; top: 150px;
    list-style: none;
    font-size: 16px;
    line-height: 24px;
  }
  .contacts li { display: flex; align-items: center; gap: 9px; }
  .contacts svg { width: 14px; height: 14px; fill: var(--name-blue); flex: none; }

  .address {
    position: absolute;
    left: 62px; top: 292px;
    font-size: 16px;
  }

  .brand {
    position: absolute;
    inset: 0;
    display: flex;
    align-items: center;
    justify-content: center;
    gap: 18px;
  }
  .brand__dot {
    width: 44px; height: 44px;
    border-radius: 50%;
    background: var(--brand-blue-deep);
  }
  .brand__name {
    font-family: "Bebas Neue", "Arial Narrow", sans-serif;
    font-size: 96px;
    line-height: 1;
    letter-spacing: 4px;
    color: var(--brand-blue-deep);
  }
</style>
</head>
<body>
  <section class="card card--front">
    <div class="identity">
      <h1 class="identity__name">Lotta Berglund</h1>
      <p class="identity__role">Chief Financial Officer (CFO)</p>
    </div>
    <div class="divider"></div>
    <ul class="contacts">
      <li>
        <svg viewBox="0 0 24 24" aria-hidden="true"><path d="M6.6 10.8a15.1 15.1 0 0 0 6.6 6.6l2.2-2.2c.3-.3.7-.4 1-.2 1.1.4 2.3.6 3.6.6.6 0 1 .4 1 1V20c0 .6-.4 1-1 1A17 17 0 0 1 3 4c0-.6.4-1 1-1h3.5c.6 0 1 .4 1 1 0 1.3.2 2.5.6 3.6.1.3 0 .7-.2 1z"/></svg>
        +46 8 52 61 74
      </li>
      <li>
        <svg viewBox="0 0 24 24" aria-hidden="true"><path d="M7 1h10a2 2 0 0 1 2 2v18a2 2 0 0 1-2 2H7a2 2 0 0 1-2-2V3a2 2 0 0 1 2-2zm0 3v14h10V4zm5 15.5a1.2 1.2 0 1 0 0 2.4 1.2 1.2 0 0 0 0-2.4z"/></svg>
        +46701 23 45 67
      </li>
      <li>
        <svg viewBox="0 0 24 24" aria-hidden="true"><path d="M2 5h20v14H2zm2 2v.5l8 5.5 8-5.5V7zm0 2.9V17h16V9.9l-8 5.5z"/></svg>
        lotta.berglund@quorenta-example.com
      </li>
      <li>
        <svg viewBox="0 0 24 24" aria-hidden="true"><path d="M12 2a10 10 0 1 0 0 20 10 10 0 0 0 0-20zm6.9 6h-3a15 15 0 0 0-1.3-4A8 8 0 0 1 18.9 8zM12 4c.8 1.2 1.5 2.5 1.9 4h-3.8c.4-1.5 1.1-2.8 1.9-4zM4.3 14a8 8 0 0 1 0-4h3.4a16 16 0 0 0 0 4zm.8 2h3a15 15 0 0 0 1.3 4A8 8 0 0 1 5.1 16zm3-8h-3a8 8 0 0 1 4.3-4 15 15 0 0 0-1.3 4zM12 20c-.8-1.2-1.5-2.5-1.9-4h3.8c-.4 1.5-1.1 2.8-1.9 4zm2.3-6H9.7a14 14 0 0 1 0-4h4.6a14 14 0 0 1 0 4zm.3 6a15 15 0 0 0 1.3-4h3a8 8 0 0 1-4.3 4zm1.7-6a16 16 0 0 0 0-4h3.4a8 8 0 0 1 0 4z"/></svg>
        www.quorenta-example.com
      </li>
    </ul>
    <p class="address">Quorenta Sweden AB Rönnvägen 14, SE-175 43 JÄRFÄLLA, Sweden</p>
  </section>

  <section class="card card--back">
    <div class="brand">
      <span class="brand__dot"></span>
      <span class="brand__name">Quorenta</span>
    </div>
  </section>
</body>
</html>
```